Catalogue Design Project

We are looking to have our product range from our website turned into a professionally printed A4 gloss catalogue.

What we require is a designer to create a front page and 3 Product pages. These 3 product pages should be from 3 separate categories. for example fabric plasters, resus & antiseptic. (your choice) You can select 4- 6 products from each category.

(we understand categories have more than 6 products, we just want to see options on how to break up the categories. such as different colors, graphics for example) It is entirely up to you.

We are looking for a stylish, professional design which is easy to follow.

our website www.tallowbrookmedical.com.au information such as photos etc is to be taken from website.

Each product should contain price, size, title & each listing on our site has 4 little images (sterile)(hypo allergenic) etc. If the product listing has these images they should be placed under each product in the catalogue.

See attached document for a very rough idea. Please note we are looking for something a lot better than this.

Target Market(s)

Mainly business, sporting clubs etc.

Industry/Entity Type

Product

Requirements
Must have
• We would like to try and keep inline with our website, we have made a real effort thus far to keep our logo and style throughout all of our print material etc.

Our business is based around First Aid Supplies, Kits & Sports Strapping tapes. These are the 3 pillars of our business.

```html
<!DOCTYPE html>
<html lang="en">
<head>
<meta charset="utf-8">
<title>Tallowbrook Medical — Product Catalogue 2013</title>
<link rel="stylesheet" href="https://fonts.googleapis.com/css2?family=Roboto+Condensed:wght@700&family=Questrial&family=Josefin+Sans:wght@300&display=swap">
<style>
  :root {
    --paper: #ffffff;
    --band-green: #abea98;
    --band-overlap: #78de5e;
    --brand-green: #3fc21c;
    --title-green: #6cd154;
    --ink-grey: #4a4f54;
    --tagline-ink: #3f4347;
  }
  html, body {
    margin: 0;
    padding: 0;
    overflow: hidden;
    background: var(--paper);
  }
  .cover {
    position: relative;
    width: 848px;
    height: 1200px;
    overflow: hidden;
    background: var(--paper);
  }
  .cover__stripe {
    position: absolute;
    left: 685px;
    top: 0;
    width: 101px;
    height: 1200px;
    background: var(--band-green);
  }
  .cover__band {
    position: absolute;
    left: 0;
    top: 1030px;
    width: 848px;
    height: 102px;
    background: var(--band-green);
  }
  .cover__crossing {
    position: absolute;
    left: 685px;
    top: 1030px;
    width: 101px;
    height: 102px;
    background: var(--band-overlap);
  }
  .brand {
    position: absolute;
    left: 62px;
    top: 390px;
  }
  .brand__mark {
    position: absolute;
    left: 395px;
    top: -60px;
    width: 86px;
    height: 86px;
    background: var(--brand-green);
  }
  .brand__name {
    margin: 0;
    font-family: "Roboto Condensed", "Arial Narrow", sans-serif;
    font-weight: 700;
    font-size: 84px;
    line-height: 76px;
    letter-spacing: -1px;
    color: var(--ink-grey);
  }
  .brand__tagline {
    margin: 14px 0 0 2px;
    font-family: "Questrial", "Century Gothic", sans-serif;
    font-size: 21px;
    letter-spacing: 1.2px;
    color: var(--tagline-ink);
    white-space: nowrap;
  }
  .brand__dot {
    display: inline-block;
    width: 7px;
    height: 7px;
    margin: 0 5px 3px 6px;
    border-radius: 50%;
    background: var(--brand-green);
    vertical-align: middle;
  }
  .cover__title {
    position: absolute;
    left: 161px;
    top: 1058px;
    margin: 0;
    font-family: "Josefin Sans", "Century Gothic", sans-serif;
    font-weight: 300;
    font-size: 45px;
    line-height: 50px;
    letter-spacing: 2.6px;
    color: var(--title-green);
    white-space: nowrap;
  }
</style>
</head>
<body>
  <main class="cover">
    <div class="cover__stripe"></div>
    <div class="cover__band"></div>
    <div class="cover__crossing"></div>

    <header class="brand">
      <span class="brand__mark"></span>
      <h1 class="brand__name">Tallowbrook<br>Medical</h1>
      <p class="brand__tagline">First Aid Supplies<span class="brand__dot"></span>Kits<span class="brand__dot"></span>Sports Strapping tapes</p>
    </header>

    <h2 class="cover__title">PRODUCT CATALOGUE 2013</h2>
  </main>
</body>
</html>
```